Newsletter-Design für Online-Versandhandel
Zielgruppe
Wir sind ein online Versand Handel mit dem Schwerpunkt auf Bio Bettwaren. Unsere Zielgruppe sind ökologisch bewusste Menschen mittleren bis höheren Alters.
Aufgabenstellung
Unsere Corporate Farbe ist vornehmlich ein sanftes Grün.
www.bettwelt-lindqvar.example
Hier eine Auswahl von Newslettern
http://newsletter.waldmoos-shop.example/u/gm.php?prm=4pTrKmZyyQ_815204736_5390418_23847
http://newslink.lodenfalt.example/u/gm.php?prm=bRx72kdfQ_962157384_3047215_81530
Bisher haben wir unsere NL als kleinen, persönlichen Text gestaltet und dazu zwei oder drei Teaser.
Den Text möchte ich beibehalten und neben meiner Unterschrift ein ein kleines persönliches Bild einfügen.
Wichtig! Wir versenden mit postfink, wir benötigen eine dafür kompatible Vorlage.

```html
<!DOCTYPE html>
<html lang="de">
<head>
<meta charset="utf-8">
<title>Newsletter Lindqvar</title>
<link href="https://fonts.googleapis.com/css2?family=Asap:ital,wght@0,400;0,700;1,700&display=swap" rel="stylesheet">
<style>
  :root {
    --bg-top: #4a6fa8;
    --bg-bottom: #c9dff9;
    --panel: #ffffff;
    --panel-border: #c3d2e4;
    --brand-green: #009a4a;
    --text-dark: #2b2b2b;
    --accent-blue: #4a6fa8;
    --photo-a: #d9c3b0;
    --photo-b: #eef1f6;
  }
  * { margin: 0; padding: 0; box-sizing: border-box; }
  html, body { width: 1200px; height: 1000px; overflow: hidden; }
  body {
    font-family: "Asap", Arial, sans-serif;
    background: linear-gradient(to bottom, var(--bg-top) 0%, var(--bg-bottom) 100%);
    position: relative;
    color: #fff;
  }
  .topbar {
    position: absolute; left: 153px; top: 6px; width: 892px;
    display: flex; justify-content: space-between;
    font-size: 12.5px; text-transform: uppercase;
  }
  .topbar .address-hint { color: #c9d6ea; }
  .topbar .shipping { font-weight: 700; color: #fff; text-shadow: 1px 1px 1px rgba(0,0,0,.45); }
  .panel {
    position: absolute; left: 150px; width: 898px;
    background: var(--panel);
    border: 3px solid var(--panel-border);
    border-radius: 3px;
  }
  .header { top: 28px; height: 141px; }
  .brand {
    position: absolute; left: 0; right: 0; top: 48px;
    display: flex; justify-content: center; align-items: center; gap: 12px;
    font-size: 44px; font-weight: 700; color: var(--brand-green); line-height: 1;
  }
  .brand .dot { width: 22px; height: 22px; border-radius: 50%; background: var(--brand-green); }
  .nav {
    position: absolute; top: 109px; left: 336px;
    font-size: 14px; font-weight: 700; color: var(--brand-green);
  }
  .nav span { position: absolute; white-space: nowrap; }
  .intro {
    position: absolute; left: 200px; width: 800px; text-align: center;
    text-shadow: 1px 1px 2px rgba(0,0,0,.5);
    font-size: 14px; line-height: 18px;
  }
  .intro h1 { font-size: 19.5px; font-weight: 700; margin-bottom: 12px; }
  .intro h2 { font-size: 15px; font-weight: 700; line-height: 18px; }
  .intro-one { top: 208px; }
  .intro-two { top: 375px; }
  .letter { top: 528px; height: 204px; color: var(--text-dark); }
  .letter .photo {
    position: absolute; left: 35px; top: 16px; width: 124px; height: 165px;
    background: linear-gradient(160deg, var(--photo-b) 0%, var(--photo-a) 55%, #8fa3c0 100%);
  }
  .letter .prev { position: absolute; left: 36px; top: 98px; font-size: 14px; color: #666; }
  .letter .body {
    position: absolute; left: 180px; top: 17px; width: 690px;
    font-size: 13.5px; line-height: 13px; text-transform: uppercase;
    text-shadow: 1px 1px 1px rgba(0,0,0,.2);
  }
  .letter .salutation { color: var(--accent-blue); font-weight: 700; margin-bottom: 16px; }
  .letter p { margin-bottom: 15px; }
  .letter .emphasis { font-weight: 700; font-style: italic; width: 590px; }
  .letter .signature {
    position: absolute; left: 180px; top: 134px; width: 216px; height: 52px;
    background: linear-gradient(90deg, #e9e9e9, #f7f7f7);
  }
  .footer {
    top: 781px; height: 110px; color: var(--text-dark);
    font-size: 12.5px; line-height: 14px; text-transform: none;
    text-shadow: 1px 1px 1px rgba(0,0,0,.2);
  }
  .footer .company { position: absolute; left: 20px; top: 19px; text-transform: uppercase; }
  .footer .contact { position: absolute; right: 20px; top: 19px; text-align: right; }
</style>
</head>
<body>
  <div class="topbar">
    <span class="address-hint">Bitte fügen Sie uns Ihrem Adressbuch hinzu</span>
    <span class="shipping">Innerhalb Deutschlands versenden wir portofrei</span>
  </div>

  <header class="panel header">
    <div class="brand"><span class="dot"></span><span>Lindqvar</span></div>
    <nav class="nav">
      <span style="left:0">HOME</span>
      <span style="left:73px">SHOP</span>
      <span style="left:149px">IMPRESSUM</span>
    </nav>
  </header>

  <section class="intro intro-one">
    <h1>Herzlich Willkommen bei Newsletter Ohne WerbeBoxen!</h1>
    <p>Kaufen Sie bei uns hochwertige, ökologische Produkte für natürliches Wohnen und gesundes Schlafen.<br>
    Bei uns finden Sie Oberbetten, Handwebteppiche, Produkte zum Schutz vor Elektrosmog, orthopädische Kissen,<br>
    Allergiker Bettdecken, Kirschkernkissen, Nackenwärmer, Daunenkissen, Kaschmirdecken.<br>
    Liegen Sie gesund und richtig in unseren Massivholzbetten, auf unseren Naturlatexmatratzen und unseren Bio<br>
    Lattenrosten. Kuscheln Sie sich in unsere ökologischen Bettwaren aus kbA Baumwolle mit den verschiedensten ....</p>
  </section>

  <section class="intro intro-two">
    <h2>Überschrift 2. Textblock</h2>
    <p>Kaufen Sie bei uns hochwertige, ökologische Produkte für natürliches Wohnen und gesundes Schlafen.<br>
    Bei uns finden Sie Oberbetten, Handwebteppiche, Produkte zum Schutz vor Elektrosmog, orthopädische Kissen,<br>
    Allergiker Bettdecken, Kirschkernkissen, Nackenwärmer, Daunenkissen, Kaschmirdecken.<br>
    Liegen Sie gesund und richtig in unseren Massivholzbetten, auf unseren Naturlatexmatratzen und unseren Bio<br>
    Lattenrosten. Kuscheln Sie sich in unsere ökologischen Bettwaren aus kbA Baumwolle mit den verschiedensten ....</p>
  </section>

  <section class="panel letter">
    <div class="photo" role="img" aria-label="Porträtfoto der Geschäftsführerin"></div>
    <span class="prev">‹</span>
    <div class="body">
      <div class="salutation">Liebe Kundinnen und Kunden,</div>
      <p>Seit rund 25 Jahren stellen wir in unserem Sortiment Natur-Produkte bester Qualität für Sie bereit – darunter eines der hochwertigsten natürlichen Betten-Programme, handgewebte Teppiche, Gesundheitsartikel und vieles mehr!</p>
      <p class="emphasis">Wir arbeiten hauptsächlich mit kleinen bis mittleren Handwerksbetrieben und fördern damit die Nachhaltigkeit.</p>
    </div>
    <div class="signature" role="img" aria-label="Handschriftliche Unterschrift"></div>
  </section>

  <footer class="panel footer">
    <div class="company">Natur-Versand<br>Lindqvar GmbH<br><br>Auenweg 12<br>79111 Talheim-Wiesen</div>
    <div class="contact">Kontakt:<br>Zentrale: 0761 555 2040<br>Fax: 0761 555 2049<br>Internet: www.bettwelt-lindqvar.example<br>EMail: info@bettwelt-lindqvar.example</div>
  </footer>
</body>
</html>
```